Vortel Business card
Let's Build Future
Professional
Rakesh Milavan
Founder
Vortel Consulting & Software Solutions, Inc.
2817 Harlow Crest Road
Willowbrook, IL 60527
rakeshm@postvela.com
please see the logo files to make it the same theme as the logo...
ai file
eps file
gif file
png logo
jpg
pdf file logo

```html
<!DOCTYPE html>
<html lang="en">
<head>
<meta charset="utf-8">
<title>Vortel Stationery Set</title>
<link rel="stylesheet" href="https://fonts.googleapis.com/css2?family=Montserrat:wght@400;600;800&display=swap">
<style>
:root{
  --board:#2b2b2b;
  --lime:#9cc823;
  --lime-dark:#7fa814;
  --paper:#ffffff;
  --grey:#8c8c8c;
  --grey-light:#d9d9d9;
  --ink:#333333;
  --label:#9a9a9a;
}
*{margin:0;padding:0;box-sizing:border-box}
html,body{width:1200px;height:343px;overflow:hidden;background:var(--board);font-family:"Montserrat",sans-serif}
.board{position:relative;width:1200px;height:343px}
.piece{position:absolute;background:var(--paper);overflow:hidden;box-shadow:0 2px 6px rgba(0,0,0,.5)}
.swoosh{position:absolute;left:0;bottom:0;width:100%}
.wordmark{font-weight:800;color:var(--lime);letter-spacing:1px;line-height:1}
.label{position:absolute;font-size:5px;color:var(--label);text-align:center;white-space:nowrap}

.brand{position:absolute;left:24px;top:36px;width:136px}
.brand .wordmark{font-size:25px}
.brand .company{font-size:4px;color:var(--lime);margin-top:4px;white-space:nowrap}
.brand .tagline{margin-top:3px;font-size:4.5px;font-weight:600;color:var(--grey)}

.card{width:70px;height:58px;left:24px}
.card-front{top:146px}
.card-back{top:232px;background:var(--lime)}
.card .wordmark{position:absolute;left:6px;top:7px;font-size:9px}
.card-back .wordmark{color:var(--paper)}
.card .details{position:absolute;left:6px;right:6px;top:21px;font-size:3.5px;color:var(--ink);line-height:1.45}
.card .details .name{font-weight:600;font-size:4.5px}
.card-back .details{color:var(--paper)}

.letterhead{width:212px;height:283px;top:24px}
.letterhead-a{left:168px}
.letterhead-b{left:400px}
.letterhead .wordmark{position:absolute;left:14px;top:14px;font-size:14px}
.letterhead .head-tag{position:absolute;left:14px;top:30px;font-size:3.5px;color:var(--grey)}
.letterhead .address{position:absolute;right:14px;top:14px;font-size:3.5px;line-height:1.5;color:var(--ink);text-align:right}

.envelope{width:223px}
.envelope-a{left:641px;top:24px;height:125px}
.envelope-b{left:641px;top:199px;height:99px}
.envelope .wordmark{position:absolute;left:10px;top:10px;font-size:11px}
.envelope .address{position:absolute;left:10px;top:24px;font-size:3.5px;line-height:1.5;color:var(--ink)}

.stack{position:absolute;left:948px;top:45px;width:221px;height:252px}
.stack .flap-env{position:absolute;left:0;width:221px;overflow:hidden;box-shadow:0 2px 6px rgba(0,0,0,.5)}
.stack .back{top:0;height:90px;background:var(--grey-light)}
.stack .middle{top:60px;height:110px;background:var(--lime)}
.stack .front{top:125px;height:127px;background:var(--paper)}
.stack svg{position:absolute;left:0;top:0;width:100%;height:100%}
</style>
</head>
<body>
<main class="board">

  <div class="brand">
    <div class="wordmark">VORTEL</div>
    <div class="company">Vortel Consulting &amp; Software Solutions, Inc.</div>
    <div class="tagline">Let's Build Future</div>
  </div>

  <section class="piece card card-front">
    <div class="wordmark">VORTEL</div>
    <div class="details">
      <div class="name">Rakesh Milavan</div>
      <div>Founder</div>
      <div>rakeshm@postvela.com</div>
    </div>
    <svg class="swoosh" viewBox="0 0 70 12" height="12" preserveAspectRatio="none" aria-hidden="true">
      <path d="M0 12 L0 5 Q35 12 70 1 L70 12 Z" fill="var(--lime)"/>
    </svg>
  </section>

  <section class="piece card card-back">
    <div class="wordmark">VORTEL</div>
    <div class="details">
      <div class="name">Rakesh Milavan</div>
      <div>2817 Harlow Crest Road</div>
      <div>Willowbrook, IL 60527</div>
    </div>
    <svg class="swoosh" viewBox="0 0 70 12" height="12" preserveAspectRatio="none" aria-hidden="true">
      <path d="M0 12 L0 7 Q35 12 70 0 L70 12 Z" fill="var(--paper)"/>
    </svg>
  </section>
  <div class="label" style="left:24px;top:304px;width:70px">Business Card</div>

  <section class="piece letterhead letterhead-a">
    <div class="wordmark">VORTEL</div>
    <div class="head-tag">Vortel Consulting &amp; Software Solutions, Inc.</div>
    <div class="address">2817 Harlow Crest Road<br>Willowbrook, IL 60527<br>rakeshm@postvela.com</div>
    <svg class="swoosh" viewBox="0 0 212 40" height="40" preserveAspectRatio="none" aria-hidden="true">
      <path d="M0 40 L0 6 Q90 38 212 22 L212 40 Z" fill="var(--lime)"/>
      <path d="M0 40 L0 20 Q100 44 212 30 L212 40 Z" fill="var(--grey)"/>
    </svg>
  </section>
  <div class="label" style="left:168px;top:313px;width:212px">Letterhead Design</div>

  <section class="piece letterhead letterhead-b">
    <div class="wordmark">VORTEL</div>
    <div class="head-tag">Vortel Consulting &amp; Software Solutions, Inc.</div>
    <div class="address">2817 Harlow Crest Road<br>Willowbrook, IL 60527<br>rakeshm@postvela.com</div>
    <svg class="swoosh" viewBox="0 0 212 26" height="26" preserveAspectRatio="none" aria-hidden="true">
      <path d="M0 26 L0 10 Q110 22 212 4 L212 26 Z" fill="var(--lime)"/>
      <path d="M0 26 L0 18 Q110 28 212 14 L212 26 Z" fill="var(--lime-dark)"/>
    </svg>
  </section>
  <div class="label" style="left:400px;top:313px;width:212px">Letterhead Design</div>

  <section class="piece envelope envelope-a">
    <div class="wordmark">VORTEL</div>
    <div class="address">2817 Harlow Crest Road<br>Willowbrook, IL 60527</div>
    <svg class="swoosh" viewBox="0 0 223 26" height="26" preserveAspectRatio="none" aria-hidden="true">
      <path d="M0 26 L0 6 Q100 26 223 10 L223 26 Z" fill="var(--lime)"/>
      <path d="M0 26 L0 18 Q110 28 223 18 L223 26 Z" fill="var(--grey)"/>
    </svg>
  </section>
  <div class="label" style="left:641px;top:154px;width:223px">Envelope Design</div>

  <section class="piece envelope envelope-b">
    <div class="wordmark">VORTEL</div>
    <div class="address">2817 Harlow Crest Road<br>Willowbrook, IL 60527</div>
    <svg class="swoosh" viewBox="0 0 223 22" height="22" preserveAspectRatio="none" aria-hidden="true">
      <path d="M0 22 L0 6 Q120 20 223 2 L223 22 Z" fill="var(--lime)"/>
    </svg>
  </section>
  <div class="label" style="left:641px;top:303px;width:223px">Envelope Design</div>

  <section class="stack" aria-label="Envelope backs">
    <div class="flap-env back">
      <svg viewBox="0 0 221 90" preserveAspectRatio="none" aria-hidden="true">
        <path d="M0 0 L221 0 L221 20 Q110 60 0 20 Z" fill="var(--grey)"/>
      </svg>
    </div>
    <div class="flap-env middle">
      <svg viewBox="0 0 221 110" preserveAspectRatio="none" aria-hidden="true">
        <path d="M0 0 L221 0 L221 24 Q110 70 0 24 Z" fill="var(--paper)"/>
        <path d="M0 24 Q110 70 221 24" fill="none" stroke="var(--lime-dark)" stroke-width="2"/>
      </svg>
    </div>
    <div class="flap-env front">
      <svg viewBox="0 0 221 127" preserveAspectRatio="none" aria-hidden="true">
        <path d="M0 0 L221 0 L221 24 Q110 74 0 24 Z" fill="var(--lime)"/>
        <path d="M0 127 L100 70 M221 127 L121 70" stroke="var(--grey-light)" stroke-width="1"/>
      </svg>
    </div>
  </section>

</main>
</body>
</html>
```